依頼詳細
商品や価格帯を口頭でしか伝えられてないので、チラシでこんな感じのものでどのくらいの価格帯かを伝えるチラシを作っていただきたいです。
記載項目
●社名:Whistling Meadow(ホイッスリング メドウ)
●電話番号:072-555-0148
●mail:whistling.meadow@mailqorvex.com
●URL:http://w-meadow-qorvex.com/
●料金プラン:
お祝い・記念日・誕生日など様々なシーンに!
バルーンアレンジメント・・\5,000~

結婚式・開店祝いなどメッセージカードをつけて!
バルーンブーケ・・・・・・\5,000~

フラワースタンドを圧倒するインパクト!
バルーンスタンド・・・・・\25,000~

各種イベントの演出に!
バルーンアーチ・・・・・・\40,000~

季節のデコレーションからプロポーズ演出まで!
バルーンデコレーション・・\50,000~

●キャッチコピー:To create a dream and smile
●ロゴ:添付ファイル
●商品写真:添付ファイル
●発送:大阪北摂エリア無料配達いたします。【バルーンギフト・ブーケは全国発送可能※一部離島を除く】
●ご予算・ご希望に応じてオリジナルでお作り致します。
作り置きはしておりません。在庫に限りがございますので、お早目のご予約をおすすめいたします。
どんなことでもお気軽にご相談下さい。
サイズ
A4
ページ数
片面
希望イメージ
シンプル 複雑
単色 カラフル
暗い 明るい
日常 高級
遊び心 厳粛
未来的 伝統的
女性的 男性的
希望する色
ロゴデザインがポップで、カラーがオレンジですが、あまり安っぽくない感じの色目でお願いします。
納品ファイル
• 高解像度JPG (.jpg)
• イラストレーター形式 (.ai)
• フォトショップ形式 (.psd)
• PNG形式 (.png)
補足説明
参考にサンプルチラシを添付します。
添付データ漏れていたのでアップします。
画象1点追加しました。(バルーンアレンジメント02)
■ 選んだ理由

たくさんの提案の中、本当に悩みに悩んで決めさせていただきました。
社員ともども色使いが落ち着いている中で上品に仕上げてくれている点を気に入り今回選ばせていただきました。

■ 提案者全員のお礼・コメント

このたびはたくさんのご提案をありがとうございました。
本当に素晴らしい作品ばかりで、悩みに悩み、決めるのに時間がかかり申し訳ございませんでした。
また、今後も色々とハコニワークを利用していきますので、またの機会によろしくお願いいたします。
本当にありがとうございました。

```html
<!DOCTYPE html>
<html lang="ja">
<head>
<meta charset="utf-8">
<title>Whistling Meadow バルーン料金案内</title>
<link rel="stylesheet" href="https://fonts.googleapis.com/css2?family=Noto+Serif+JP:wght@400;700&family=Noto+Sans+JP:wght@400;700&family=Noto+Serif:wght@400&display=swap">
<style>
  :root{
    --orange:#ee6a1f;
    --orange-deep:#d9560f;
    --cream:#fff6ea;
    --ink:#3a2418;
    --white:#ffffff;
  }
  *{margin:0;padding:0;box-sizing:border-box}
  html,body{width:847px;height:1200px;overflow:hidden;background:var(--orange)}
  .flyer{position:relative;width:847px;height:1200px;background:var(--orange);overflow:hidden;font-family:"Noto Sans JP",sans-serif;color:var(--white)}
  .tagline{position:absolute;left:22px;top:40px;height:980px;writing-mode:vertical-rl;font-family:"Noto Serif",serif;font-size:50px;letter-spacing:4px;line-height:60px;color:var(--cream);white-space:nowrap}
  .hero-photo{position:absolute;left:140px;top:0;width:320px;height:1130px;background:linear-gradient(180deg,#3a1c1c 0%,#c8261f 35%,#b8325a 65%,#2a1a1a 100%)}
  .product-photo{position:absolute;border-radius:50%;border:3px solid var(--white)}
  .bubble{position:absolute;border-radius:50%;background:var(--white);color:var(--ink);display:flex;flex-direction:column;align-items:center;justify-content:center;text-align:center;font-size:9.5px;line-height:1.45;padding:16px}
  .bubble .price{font-family:"Noto Serif",serif;font-size:11px;color:var(--orange-deep);margin-top:2px}
  .notes{position:absolute;left:564px;top:848px;width:270px}
  .notes .lead{font-family:"Noto Serif JP",serif;font-weight:700;font-size:15px;line-height:1.4}
  .notes .lead.big{font-size:16.5px;margin-top:10px}
  .notes .small{font-size:8.5px;line-height:1.55;margin-top:2px}
  .brand{position:absolute;left:452px;top:1076px;display:flex;align-items:center;gap:8px;font-family:"Noto Serif",serif;font-size:22px;color:var(--ink)}
  .brand .dot{width:18px;height:18px;border-radius:50%;background:var(--ink)}
  .contact{position:absolute;left:450px;top:1112px;width:384px;height:78px;border:2px solid var(--white);border-radius:8px;background:rgba(255,255,255,.12);padding:5px 14px;font-family:"Noto Serif",serif;font-size:14px;line-height:22px;color:var(--white)}
  .consult{position:absolute;left:14px;top:1074px;width:128px;height:112px;border-radius:50%;background:var(--white);color:var(--orange-deep);display:flex;align-items:center;justify-content:center;text-align:center;font-weight:700;font-size:12px;line-height:1.5}
</style>
</head>
<body>
<main class="flyer">
  <p class="tagline">To create a dream and smile</p>

  <div class="hero-photo" role="img" aria-label="赤と黒を基調にしたバルーンスタンドとバルーンアレンジメントの商品写真"></div>

  <div class="product-photo" role="img" aria-label="バルーンアレンジメントの写真" style="left:690px;top:14px;width:142px;height:142px;background:radial-gradient(circle,#f4c6d8,#b25ab0)"></div>
  <div class="bubble" style="left:570px;top:14px;width:124px;height:124px">お祝い・記念日・誕生日など様々なシーンに！<span class="price">¥5,000~</span></div>

  <div class="product-photo" role="img" aria-label="バルーンブーケとメッセージカードの写真" style="left:636px;top:205px;width:180px;height:180px;background:radial-gradient(circle,#f7f1e6,#e0a24a)"></div>
  <div class="bubble" style="left:500px;top:200px;width:132px;height:132px">結婚式・開店祝いなどメッセージカードをつけて！<span class="price">¥5,000~</span></div>

  <div class="product-photo" role="img" aria-label="バルーンスタンドの写真" style="left:506px;top:520px;width:130px;height:130px;background:radial-gradient(circle,#d8f0ea,#3f9a8a)"></div>
  <div class="bubble" style="left:640px;top:462px;width:130px;height:130px">フラワースタンドを圧倒するインパクト！<span class="price">¥25,000~</span></div>

  <div class="bubble" style="left:510px;top:664px;width:136px;height:136px">各種イベント用、デコレーションからプロポーズ演出まで<span class="price">¥40,000~</span></div>
  <div class="product-photo" role="img" aria-label="バルーンアーチとデコレーションの写真" style="left:664px;top:664px;width:168px;height:178px;border-radius:8px;background:radial-gradient(circle,#f3e4d0,#c94a3a)"></div>

  <section class="notes">
    <p class="lead">大阪北摂エリア無料配達いたします。</p>
    <p class="small">【バルーンギフト・ブーケは全国発送可能※一部離島を除く】</p>
    <p class="lead big">ご予算・ご希望に応じて<br>オリジナルでお作り致します。</p>
    <p class="small">作り置きはしておりません。在庫に限りがございますので、お早目のご予約をおすすめいたします。</p>
  </section>

  <div class="brand"><span class="dot"></span>Whistling Meadow</div>

  <section class="contact">
    <p>telephone : 072-555-0148</p>
    <p>mail : whistling.meadow@mailqorvex.com</p>
    <p>WEB : http://w-meadow-qorvex.com/</p>
  </section>

  <p class="consult">どんなことでも<br>お気軽に<br>ご相談下さい！</p>
</main>
</body>
</html>
```